Promotional brochure for educational consulting firm

Hi Designers!

Please do a 8.5 x 11 inch tri-fold brochure as well as a 8.5 x 11 inch half-fold brochure.  I appreciate black and white versions in addition to color.  Please take a look at my company's website for a better sense of the look and feel I am going for:  www.brightlarkedu.org

Thanks!

Industry/Entity Type

Consulting

Colors
3176b5
85abd2
fcfbfd

```html
<!DOCTYPE html>
<html lang="en">
<head>
<meta charset="utf-8">
<title>Brightlark Associates – Tri-fold Brochure</title>
<link href="https://fonts.googleapis.com/css2?family=Quicksand:wght@500;600;700&family=PT+Sans:wght@400;700&display=swap" rel="stylesheet">
<style>
  :root {
    --brand-blue: #3176b5;
    --deep-blue: #1f5c99;
    --soft-blue: #85abd2;
    --paper: #fcfbfd;
    --ink: #22303d;
    --ink-soft: #3a3f46;
    --stage: #e6e7ea;
  }
  * { box-sizing: border-box; margin: 0; padding: 0; }
  html, body { width: 1200px; height: 1000px; overflow: hidden; }
  body { background: var(--stage); font-family: "PT Sans", Arial, sans-serif; position: relative; }

  .brochure {
    position: absolute; left: 50px; top: 140px; width: 1100px; height: 720px;
    background: var(--paper); box-shadow: 0 10px 30px rgba(0,0,0,.18);
    display: flex; overflow: hidden;
  }
  .panel { position: relative; width: 366.67px; height: 100%; overflow: hidden; }
  .panel + .panel { border-left: 1px solid rgba(0,0,0,.06); }

  .headline {
    position: absolute; left: 36px; top: 28px; width: 680px; z-index: 3;
    font-family: "Quicksand", sans-serif; font-weight: 700; font-size: 26px; line-height: 1.2;
    color: var(--ink-soft);
  }
  .headline .brand { color: var(--brand-blue); }

  .photo { position: absolute; }
  .photo-reading { left: 0; top: 118px; width: 100%; height: 270px;
    background: linear-gradient(135deg, #5a3f36 0%, #c9a27a 45%, #d9c7b0 70%, #8b5a6e 100%); }
  .photo-globe { left: 0; top: 0; width: 100%; height: 245px;
    background: linear-gradient(120deg, #e8eef3 0%, #4f86b8 35%, #2a2233 65%, #1e1a2a 100%); }

  .wave { position: absolute; left: 0; width: 100%; display: block; }
  .blue-field { position: absolute; left: 0; width: 100%; background: var(--brand-blue); }

  .intro-title {
    position: absolute; left: 34px; top: 392px; z-index: 2;
    font-family: "Quicksand", sans-serif; font-weight: 700; font-size: 23px; color: var(--ink);
  }
  .intro-copy {
    position: absolute; left: 34px; top: 440px; width: 305px; z-index: 2;
    font-family: "Quicksand", sans-serif; font-weight: 700; font-size: 15px; line-height: 1.8;
    color: var(--paper);
  }

  .question-icon { position: absolute; left: 150px; top: 112px; }
  .questions { position: absolute; left: 30px; width: 310px; z-index: 2;
    font-family: "PT Sans", sans-serif; font-size: 15px; line-height: 1.45; }
  .questions p { margin-bottom: 15px; }
  .questions.on-paper { top: 168px; color: var(--ink-soft); }
  .questions.on-blue { top: 418px; color: var(--paper); }

  .bio-title { position: absolute; left: 30px; top: 268px; z-index: 2;
    font-family: "Quicksand", sans-serif; font-weight: 700; font-size: 17px; color: var(--ink); }
  .bio-copy { position: absolute; left: 30px; top: 294px; width: 310px; z-index: 2;
    font-family: "Quicksand", sans-serif; font-weight: 600; font-size: 14.5px; line-height: 1.75; color: var(--paper); }

  .expertise-title { position: absolute; left: 30px; top: 518px; z-index: 2;
    font-family: "Quicksand", sans-serif; font-weight: 700; font-size: 23px; line-height: 1.05; color: var(--brand-blue); }
  .expertise-list { position: absolute; top: 584px; z-index: 2; list-style: none;
    font-family: "PT Sans", sans-serif; font-size: 13px; color: var(--ink); }
  .expertise-list.col-a { left: 30px; width: 160px; }
  .expertise-list.col-b { left: 190px; width: 160px; top: 566px; }
  .expertise-list li { position: relative; padding-left: 30px; margin-bottom: 9px; line-height: 1.25; }
  .expertise-list li::before { content: "»"; position: absolute; left: 4px; top: -2px; font-size: 16px; color: var(--ink); }
</style>
</head>
<body>
  <main class="brochure">
    <h1 class="headline"><span class="brand">Brightlark Associates</span> provides just-in-time support<br>to schools and school leaders.</h1>

    <section class="panel panel-intro">
      <div class="photo photo-reading" role="img" aria-label="Photo of a student reading a book in a classroom"></div>
      <svg class="wave" style="top:100px" width="367" height="60" viewBox="0 0 367 60" preserveAspectRatio="none">
        <path d="M0 24 Q180 10 367 40 L367 58 Q180 30 0 38 Z" fill="var(--deep-blue)"/>
      </svg>
      <svg class="wave" style="top:340px" width="367" height="60" viewBox="0 0 367 60" preserveAspectRatio="none">
        <path d="M0 30 Q180 0 367 10 L367 60 L0 60 Z" fill="var(--brand-blue)"/>
      </svg>
      <div class="blue-field" style="top:395px;height:325px"></div>
      <h2 class="intro-title">Brightlark Associates LLC</h2>
      <p class="intro-copy">Schools along the continuum of organizational growth—from startup schools to developing or mature schools—can benefit from specialized expertise to complete a time-sensitive special project or develop strategies and processes to take their program to the next level of excellence. Our team of expert associates is ready to assist you.</p>
    </section>

    <section class="panel panel-questions">
      <svg class="question-icon" width="48" height="44" viewBox="0 0 48 44" aria-hidden="true">
        <rect x="3" y="6" width="38" height="32" rx="4" fill="#fff" stroke="var(--brand-blue)" stroke-width="3"/>
        <text x="22" y="32" text-anchor="middle" font-family="Quicksand, sans-serif" font-weight="700" font-size="26" fill="var(--brand-blue)">?</text>
      </svg>
      <div class="questions on-paper">
        <p>How do I develop a high-functioning board?</p>
        <p>What policies do start-up schools need to have on day one?</p>
        <p>Is my meal program optimizing revenue?</p>
        <p>We want to refinance our property. How do we tell our story to a lender?</p>
      </div>
      <svg class="wave" style="top:368px" width="367" height="40" viewBox="0 0 367 40" preserveAspectRatio="none">
        <path d="M0 20 Q180 6 367 14 L367 40 L0 40 Z" fill="var(--brand-blue)"/>
      </svg>
      <div class="blue-field" style="top:406px;height:314px"></div>
      <div class="questions on-blue">
        <p>How can we increase parent engagement?</p>
        <p>What do we need to do to increase visibility (and enrollment)?</p>
        <p>My assistant principal is going out on extended leave… can I get someone to step in while he's out?</p>
        <p>Do these questions keep you up at night? If so, we can help.</p>
      </div>
    </section>

    <section class="panel panel-expertise">
      <div class="photo photo-globe" role="img" aria-label="Photo of two students examining a globe with a magnifying glass"></div>
      <svg class="wave" style="top:205px" width="367" height="60" viewBox="0 0 367 60" preserveAspectRatio="none">
        <path d="M0 40 Q180 10 367 8 L367 60 L0 60 Z" fill="var(--deep-blue)"/>
        <path d="M0 52 Q180 24 367 22 L367 60 L0 60 Z" fill="var(--brand-blue)"/>
      </svg>
      <div class="blue-field" style="top:264px;height:240px"></div>
      <svg class="wave" style="top:470px" width="367" height="60" viewBox="0 0 367 60" preserveAspectRatio="none">
        <path d="M0 30 L160 14 L178 0 L190 14 L367 6 L367 60 L0 60 Z" fill="var(--paper)"/>
      </svg>
      <h3 class="bio-title">Education + Business</h3>
      <p class="bio-copy">My 10-year experience as an executive director of charter schools in the two largest school districts in California gives me a unique “education + business” perspective in addition to a network of on-call, expert associates who are ready to assist your school in a variety of key areas.</p>
      <h3 class="expertise-title">Our areas of expertise<br>include:</h3>
      <ul class="expertise-list col-a">
        <li>Board Training</li>
        <li>Budget and Operations</li>
        <li>Charter Development</li>
        <li>Communications</li>
      </ul>
      <ul class="expertise-list col-b">
        <li>Leadership Coaching</li>
        <li>Lender Negotiations</li>
        <li>Fund Development</li>
        <li>Placement of interim administrators</li>
      </ul>
    </section>
  </main>
</body>
</html>
```